Hip surgeon needs a stationery design

I need a new stationery design for my private practice.
My practice is focused in hip arthroplasty (hip prosthesis).
I'd like to see designs most in blue or shades of blue.
I've uploaded my new logo to help with the task.
Also, I'm a member of some societies and I've uploaded their logos either, so I'd like to see them in some of the stationeries.
Itens list:
business card
letterhead A4
envelope
prescription block A5
one fold for A4 (please see the archive "pocket")
Personal data:
Dr. Renan L. Vasconti
CRM/PR 57316
site: www.clinicapelvora.com.br
email: dr.renan@clinicapelvora.com.br
Adress:
Rua Leopoldo Marques Vieira de Lima, 712
Campo Sereno - Curitiba/PR
41 30875316 I 30875317
Updates
I forgot to mention that my practice is focused primarily in hip arthroplasty (total hip prosthesis) and the target audience range from young adults to the elderly.
I also perform hip preserving surgeries (open and arthroscopic procedures) and pelvic and hip fracture surgery (trauma).
- Any "cleaner" fonts are welcome

```html
<!DOCTYPE html>
<html lang="pt-BR">
<head>
<meta charset="utf-8">
<title>Dr. Renan L. Vasconti – Papelaria</title>
<link href="https://fonts.googleapis.com/css2?family=Roboto+Condensed:wght@400;700&family=Open+Sans:wght@400;600;700&display=swap" rel="stylesheet">
<style>
  :root{
    --stage:#0f5a9c;
    --blue:#2a86f6;
    --cyan:#1de9f4;
    --sky:#18b9f6;
    --ink:#333a40;
    --paper:#ffffff;
    --fold:#e6e7ea;
    --faint:rgba(255,255,255,.16);
    --faint-blue:rgba(42,134,246,.07);
  }
  *{margin:0;padding:0;box-sizing:border-box}
  html,body{width:1200px;height:1000px;overflow:hidden;background:var(--stage)}
  .canvas{position:relative;width:1200px;height:1000px;background:var(--stage);font-family:"Open Sans",sans-serif;color:var(--ink)}
  .sheet{position:absolute;background:var(--paper);overflow:hidden;box-shadow:0 6px 18px rgba(0,0,0,.25)}

  /* brand lockup */
  .lockup{position:absolute;display:flex;align-items:center;gap:8px}
  .lockup .dot{border-radius:50%;flex:none}
  .lockup .name{font-family:"Roboto Condensed",sans-serif;font-weight:400;line-height:1.05;white-space:nowrap}
  .lockup .tag{font-family:"Roboto Condensed",sans-serif;font-weight:400;line-height:1.1;white-space:nowrap}
  .faint-ring{position:absolute;border-radius:50%}

  /* folder cover */
  .folder-cover{left:47px;top:43px;width:341px;height:481px;background:linear-gradient(180deg,var(--blue),var(--cyan));z-index:2}
  .folder-cover .dot{width:48px;height:48px;background:#fff}
  .folder-cover .name{font-size:18px;color:#fff}
  .folder-cover .tag{font-size:12.5px;color:#fff}
  /* folder inside */
  .folder-back{left:83px;top:66px;width:342px;height:482px;background:var(--fold);box-shadow:none}
  .folder-inside{left:425px;top:66px;width:340px;height:482px}
  .pocket{position:absolute;left:0;top:337px;width:340px;height:145px}
  .folder-inside .lockup{left:57px;top:357px;z-index:2}
  .folder-inside .dot{width:46px;height:46px;background:#fff}
  .folder-inside .name{font-size:17px;color:#fff}
  .folder-inside .tag{font-size:12px;color:#fff}

  /* letterhead */
  .letterhead{left:807px;top:66px;width:341px;height:482px}
  .letterhead .dot{width:32px;height:32px;background:var(--blue)}
  .letterhead .name{font-size:12.5px;color:var(--blue)}
  .letterhead .tag{font-size:9px;color:var(--sky)}
  .letter-body{position:absolute;left:39px;top:84px;width:292px;font-size:6px;line-height:7.5px;color:#444}
  .letter-body p{margin-bottom:7px}
  .letter-body .copy{text-align:justify;hyphens:auto}
  .signature{position:absolute;left:44px;top:302px;width:64px;height:58px;border-radius:4px;background:linear-gradient(135deg,rgba(42,134,246,.18),rgba(42,134,246,.05))}
  .contact{position:absolute;font-size:4.6px;line-height:6px;color:#333;white-space:nowrap}
  .contact .site{font-family:"Open Sans",sans-serif;font-weight:700;font-size:7px;color:var(--blue);line-height:9px}

  /* prescription */
  .prescription{left:61px;top:582px;width:255px;height:360px}
  .prescription .dot{width:26px;height:26px;background:var(--blue)}
  .prescription .name{font-size:10.5px;color:var(--blue)}
  .prescription .tag{font-size:7.5px;color:var(--sky)}
  .crm-band{position:absolute;left:0;top:46px;width:255px;height:12px;background:var(--sky);color:#fff;font-family:"Roboto Condensed",sans-serif;font-size:9px;line-height:12px;padding-left:24px}
  .patient-line{position:absolute;left:16px;top:70px;font-size:4.4px;color:#888;white-space:nowrap}
  .patient-line span{display:inline-block;border-bottom:.5px solid #aaa;margin-right:4px}
  .badges{position:absolute;left:145px;top:323px;display:flex;gap:6px;align-items:center}
  .badge-grey{width:58px;height:20px;border-radius:2px;background:#6d6f73}
  .badge-green{width:26px;height:20px;border-radius:3px;background:#43b649}

  /* envelopes */
  .envelope-back{left:368px;top:582px;width:437px;height:218px}
  .envelope-flap{position:absolute;left:0;top:0;width:437px;height:70px;background:var(--sky);border-radius:0 0 10px 10px}
  .envelope-back .dot{width:42px;height:42px;background:#fff}
  .envelope-back .name{font-size:14px;color:#fff}
  .envelope-back .tag{font-size:11px;color:#fff}
  .envelope-front{left:426px;top:718px;width:436px;height:218px}
  .envelope-front .dot{width:38px;height:38px;background:var(--blue)}
  .envelope-front .name{font-size:14px;color:var(--blue)}
  .envelope-front .tag{font-size:11px;color:var(--sky)}
  .window{position:absolute;left:30px;top:102px;width:201px;height:82px;border-radius:8px;background:var(--sky)}

  /* business cards */
  .card-front{left:907px;top:619px;width:103px;height:180px}
  .card-front .mark{position:absolute;left:24px;top:17px;width:56px;height:56px;border-radius:50%;background:linear-gradient(180deg,var(--blue),var(--cyan))}
  .card-text{position:absolute;left:15px;top:92px;font-size:3.8px;line-height:4.8px;color:#555}
  .card-text .cname{font-family:"Roboto Condensed",sans-serif;font-size:6.5px;color:var(--blue);line-height:7px}
  .card-text .ctag{font-family:"Roboto Condensed",sans-serif;font-size:4.8px;color:var(--sky);margin-bottom:6px}
  .card-text .email{color:var(--blue);margin:6px 0}
  .card-back{left:1033px;top:728px;width:103px;height:180px;background:linear-gradient(180deg,var(--blue),var(--cyan))}
  .card-back .mark{position:absolute;left:29px;top:49px;width:45px;height:45px;border-radius:50%;background:#fff}
  .card-back .url{position:absolute;left:0;top:99px;width:103px;text-align:center;font-size:4.6px;font-weight:700;color:#fff}
</style>
</head>
<body>
<div class="canvas">

  <!-- folder inside -->
  <div class="sheet folder-back"></div>
  <div class="sheet folder-inside">
    <svg class="pocket" viewBox="0 0 340 145" aria-hidden="true">
      <defs>
        <linearGradient id="pocketFill" x1="0" y1="0" x2="0" y2="1">
          <stop offset="0" stop-color="#18c6f6"/>
          <stop offset="1" stop-color="#06e4f3"/>
        </linearGradient>
      </defs>
      <path d="M58 0 H340 V145 H0 L30 28 Q38 0 58 0 Z" fill="url(#pocketFill)"/>
      <circle cx="290" cy="110" r="70" fill="rgba(255,255,255,.14)"/>
    </svg>
    <div class="lockup">
      <span class="dot"></span>
      <div><div class="name">Dr. Renan L. Vasconti</div><div class="tag">Cirurgia do Quadril</div></div>
    </div>
  </div>

  <!-- folder cover -->
  <div class="sheet folder-cover">
    <div class="faint-ring" style="left:115px;top:260px;width:260px;height:260px;background:var(--faint)"></div>
    <div class="lockup" style="left:28px;top:22px">
      <span class="dot"></span>
      <div><div class="name">Dr. Renan L. Vasconti</div><div class="tag">Cirurgia do Quadril</div></div>
    </div>
  </div>

  <!-- letterhead -->
  <div class="sheet letterhead">
    <div class="faint-ring" style="left:205px;top:355px;width:170px;height:170px;background:var(--faint-blue)"></div>
    <div class="lockup" style="left:25px;top:24px;gap:5px">
      <span class="dot"></span>
      <div><div class="name">Dr. Renan L. Vasconti</div><div class="tag">Cirurgia do Quadril</div></div>
    </div>
    <div class="letter-body">
      <p>Lorem 24, 2014</p>
      <p>Lorem ipsum dolor sit amet<br>consectetur 1234 Nullam</p>
      <p>Lorem ipsum dolor:</p>
      <p class="copy">Lorem ipsum dolor sit amet, consectetur adipiscing elit. Donec orci purus, luctus vitae dignissim eu, iaculis sed purus. Vivamus faucibus, ipsum nec aliquet viverra, leo mauris condimentum ligula, sit amet sagittis enim ligula quis arcu. Nam egestas tortor id nisi porttitor mattis. In tortor ante, ultricies in suscipit a, tempus non massa. Vivamus et auctor mi. Fusce vel massa nulla. Phasellus nec eros mauris, et scelerisque orci. Donec malesuada orci vitae nulla accumsan porta a id massa. Quisque accumsan iaculis magna sit amet fringilla. Maecenas consequat, magna eget tincidunt semper, odio nibh rutrum mi, id feugiat ante nisi eu risus. Vestibulum nunc orci, rhoncus a placerat in, ultricies in mi. Cras mattis varius eros, vel fringilla nisi suscipit eget.</p>
      <p class="copy">Quisque scelerisque sagittis nulla at porttitor. Mauris a justo et tellus interdum tristique. Sed id augue vitae urna euismod commodo aliquet a quam. Pellentesque arcu velit, cursus et malesuada ut, consequat et diam. Nullam erat sem, rhoncus id ullamcorper vitae, rhoncus et arcu. In ultricies ultricies nulla, ut rutrum nisi iaculis at. Donec eu magna a metus ornare faucibus. Fusce aliquet faucibus ultricies. Morbi semper, est id tincidunt gravida, sem arcu adipiscing lacus, ac bibendum nulla leo eu purus. Quisque nec diam sed risus consectetur accumsan quis quis nibh. Vestibulum id purus lorem.</p>
    </div>
    <div class="signature" role="img" aria-label="Handwritten signature of the doctor"></div>
    <div class="contact" style="left:39px;top:432px">
      <div class="site">www.clinicapelvora.com.br</div>
      Rua Leopoldo Marques Vieira de Lima, 712<br>
      Campo Sereno - Curitiba/PR<br>
      41 30875316 I 30875317
    </div>
  </div>

  <!-- prescription pad -->
  <div class="sheet prescription">
    <div class="faint-ring" style="left:150px;top:252px;width:150px;height:150px;background:var(--faint-blue)"></div>
    <div class="lockup" style="left:25px;top:11px;gap:4px">
      <span class="dot"></span>
      <div><div class="name">Dr. Renan L. Vasconti</div><div class="tag">Cirurgia do Quadril</div></div>
    </div>
    <div class="crm-band">CRM/PR 57316</div>
    <div class="patient-line">Patients Name <span style="width:70px"></span> Age <span style="width:22px"></span> M·F Date <span style="width:34px"></span></div>
    <div class="contact" style="left:16px;top:312px">
      <div class="site">www.clinicapelvora.com.br</div>
      Rua Leopoldo Marques Vieira de Lima, 712<br>
      Campo Sereno - Curitiba/PR<br>
      41 30875316 I 30875317
    </div>
    <div class="badges">
      <span class="badge-grey"></span>
      <span class="badge-green"></span>
    </div>
  </div>

  <!-- envelope back -->
  <div class="sheet envelope-back">
    <div class="envelope-flap"></div>
    <div class="lockup" style="left:22px;top:11px;gap:7px">
      <span class="dot"></span>
      <div><div class="name">Dr. Renan L. Vasconti</div><div class="tag">Cirurgia do Quadril</div></div>
    </div>
  </div>

  <!-- envelope front -->
  <div class="sheet envelope-front">
    <div class="lockup" style="left:30px;top:24px;gap:6px">
      <span class="dot"></span>
      <div><div class="name">Dr. Renan L. Vasconti</div><div class="tag">Cirurgia do Quadril</div></div>
    </div>
    <div class="contact" style="left:270px;top:25px">
      <div class="site">www.clinicapelvora.com.br</div>
      Rua Leopoldo Marques Vieira de Lima, 712<br>
      Campo Sereno - Curitiba/PR<br>
      41 30875316 I 30875317
    </div>
    <div class="window"></div>
  </div>

  <!-- business card front -->
  <div class="sheet card-front">
    <span class="mark"></span>
    <div class="card-text">
      <div class="cname">Dr. Renan L. Vasconti</div>
      <div class="ctag">Cirurgia do Quadril</div>
      41 30875316<br>30875317
      <div class="email">dr.renan@clinicapelvora.com.br</div>
      Rua Leopoldo Marques<br>Vieira de Lima,<br>712 Campo Sereno - Curitiba/PR
    </div>
  </div>

  <!-- business card back -->
  <div class="sheet card-back">
    <span class="mark"></span>
    <div class="url">www.clinicapelvora.com.br</div>
  </div>

</div>
</body>
</html>
```